Energy Company needs a Business Card Design

We need a business card design for a new company based in Singapore called Kavu Energy. Kavu Energy is a producer of renewable energies largely for the biofuels market. Sourced entirely from sustainable resources, Kavu Energy aims to be a fully integrated oil company operating in 100% sustainable way. We would like to see designs that use the same colours as the attached file.

Industry/Entity Type

Business

```html
<!DOCTYPE html>
<html lang="en">
<head>
<meta charset="utf-8">
<title>Kavu Energy — Business Card</title>
<link rel="stylesheet" href="https://fonts.googleapis.com/css2?family=Open+Sans:wght@300;400;600;700&display=swap">
<style>
  :root {
    --canvas: #e6e6e6;
    --card-white: #ffffff;
    --card-dark: #2c2c2e;
    --card-dark-soft: #3a3a3d;
    --brand-green: #8dc63f;
    --brand-grey: #c9c9cb;
    --ink: #4a4a4c;
    --ink-soft: #6d6d70;
  }
  * { box-sizing: border-box; margin: 0; padding: 0; }
  html, body {
    width: 1200px;
    height: 800px;
    overflow: hidden;
    background: var(--canvas);
    font-family: "Open Sans", Arial, sans-serif;
  }
  .canvas {
    width: 1200px;
    height: 800px;
    display: flex;
    flex-direction: column;
    align-items: center;
    justify-content: center;
    gap: 56px;
  }
  .card {
    width: 560px;
    height: 320px;
    position: relative;
    box-shadow: 0 6px 18px rgba(0,0,0,0.18);
    overflow: hidden;
  }

  /* Front */
  .card--front {
    background: var(--card-white);
    padding: 34px 40px;
    display: flex;
    flex-direction: column;
    align-items: flex-end;
    text-align: right;
  }
  .brand {
    display: flex;
    align-items: center;
    gap: 10px;
    color: var(--brand-green);
    font-weight: 600;
    letter-spacing: 0.06em;
    text-transform: uppercase;
  }
  .brand__dot {
    width: 12px;
    height: 12px;
    border-radius: 50%;
    background: var(--brand-green);
  }
  .card--front .brand { font-size: 24px; }
  .contact-block { margin-top: 44px; }
  .person__name {
    font-size: 26px;
    font-weight: 700;
    color: var(--ink);
    line-height: 1.1;
  }
  .person__role {
    font-size: 12px;
    font-weight: 400;
    color: var(--brand-green);
    letter-spacing: 0.04em;
    margin-top: 3px;
  }
  .contact-list {
    list-style: none;
    margin-top: 16px;
    font-size: 14px;
    color: var(--ink-soft);
    line-height: 1.65;
  }
  .contact-list li {
    display: flex;
    align-items: center;
    justify-content: flex-end;
    gap: 8px;
  }
  .contact-list strong { font-weight: 700; color: var(--ink); }
  .contact-icon {
    width: 13px;
    height: 13px;
    flex: none;
  }

  /* Back */
  .card--back {
    background: var(--card-dark);
    display: flex;
    align-items: center;
    justify-content: center;
  }
  .card__texture {
    position: absolute;
    inset: 0;
    background: radial-gradient(ellipse at 58% 50%, var(--card-dark-soft) 0%, var(--card-dark) 62%);
  }
  .card--back .brand {
    position: relative;
    font-size: 40px;
    color: var(--brand-grey);
  }
  .card--back .brand__dot {
    width: 16px;
    height: 16px;
  }
</style>
</head>
<body>
<main class="canvas">

  <section class="card card--front" aria-label="Business card front">
    <div class="brand">
      <span class="brand__name">Kavu Energy</span>
      <span class="brand__dot"></span>
    </div>
    <div class="contact-block">
      <h1 class="person__name">Daniel Tan</h1>
      <p class="person__role">MANAGING DIRECTOR</p>
      <ul class="contact-list">
        <li>+ 65 555 555 00
          <svg class="contact-icon" viewBox="0 0 14 14" aria-hidden="true">
            <rect width="14" height="14" rx="2" fill="#8dc63f"/>
            <rect x="4.5" y="2.5" width="5" height="9" rx="1" fill="none" stroke="#fff" stroke-width="1.2"/>
          </svg>
        </li>
        <li>daniel@<strong>kavuenergy</strong>.com
          <svg class="contact-icon" viewBox="0 0 14 14" aria-hidden="true">
            <rect width="14" height="14" rx="2" fill="#8dc63f"/>
            <rect x="2.5" y="4" width="9" height="6" fill="none" stroke="#fff" stroke-width="1.1"/>
            <path d="M2.5 4 L7 7.5 L11.5 4" fill="none" stroke="#fff" stroke-width="1.1"/>
          </svg>
        </li>
        <li>www.<strong>kavuenergy</strong>.com
          <svg class="contact-icon" viewBox="0 0 14 14" aria-hidden="true">
            <circle cx="7" cy="7" r="7" fill="#8dc63f"/>
            <circle cx="7" cy="7" r="4" fill="none" stroke="#fff" stroke-width="1.1"/>
            <path d="M3 7 H11 M7 3 V11" stroke="#fff" stroke-width="1.1"/>
          </svg>
        </li>
      </ul>
    </div>
  </section>

  <section class="card card--back" aria-label="Business card back">
    <div class="card__texture" role="img" aria-label="Soft halftone dot texture behind the company name"></div>
    <div class="brand">
      <span class="brand__name">Kavu Energy</span>
      <span class="brand__dot"></span>
    </div>
  </section>

</main>
</body>
</html>
```